Postcard Design www.steadfieldclaimsdesk.com

We need a new postcard design that would show our over 25 years of knowledge and expertise, yet touch on the functions and services we can perform, in Medical Billing. The problem is that the competition is fierce, with many many new Medical Billing Companies getting in the act. Unfortunately these companies can be extremely hurtful to the financial well being of medical providers, as they do not know the laws, regulations, nor have the expertise.
Updates

I just received my final approval on my trademark, so the phrase Where Patience Pays & Precision Prevails is now a registered trademark. Also I just realized on my original postcard there is a typo. It should read Over 25 years in claims, billing, and revenue recovery, the "the" should not be there. Also I would like the "free 10 chart/EOB audit" to be a bigger deal that would catch the readers eye, maybe an expiration date or some other "call to action"

Target Market(s)

Target business is medical professionals. Chiropractors, Home Health providers, providers that would have large insurance clientele (Vitacover, PPO).
NOT targeting Familiy Practice, Pediatricians, Hospitals, Dentists.

Industry/Entity Type

Financial

Font styles to use
Serif
Sans Serif

Colors
ec1f27
3277b5
ffffff

Requirements
Must have
• New ideas not just copied from my existing postcard. Something that somehow tells the story of going with inexperience can cost you.

```html
<!DOCTYPE html>
<html lang="en">
<head>
<meta charset="utf-8">
<title>Steadfield Claims Desk Postcard</title>
<link href="https://fonts.googleapis.com/css2?family=Merriweather:ital,wght@0,700;0,900;1,400&family=Source+Sans+3:wght@400;600;700;800&display=swap" rel="stylesheet">
<style>
  :root {
    --paper: #ffffff;
    --red: #ec1f27;
    --red-deep: #c8141b;
    --blue: #3277b5;
    --blue-deep: #225a8c;
    --blue-soft: #e8f1f9;
    --red-soft: #fdecec;
    --ink: #1f2a3a;
    --rule: #d4d4d4;
  }
  * { margin: 0; padding: 0; box-sizing: border-box; }
  html, body { width: 1200px; height: 930px; overflow: hidden; background: var(--paper); }
  .postcard { position: relative; width: 1200px; height: 930px; background: var(--paper); font-family: "Source Sans 3", Arial, sans-serif; color: var(--ink); }

  .promo { position: absolute; left: 0; top: 0; width: 579px; height: 742px; background: var(--paper); overflow: hidden; }

  .team-photo {
    position: absolute; left: 0; top: 0; width: 579px; height: 176px;
    background: linear-gradient(180deg, #f3f7fb 0%, #c9dcee 60%, #7fa9d2 100%);
  }
  .audit-seal { position: absolute; left: 446px; top: 64px; width: 124px; height: 124px; }

  .headline { position: absolute; left: 28px; top: 192px; width: 530px; }
  .headline h1 { font-family: "Merriweather", Georgia, serif; font-weight: 900; font-size: 30px; line-height: 38px; color: var(--blue-deep); }
  .headline p { margin-top: 4px; font-size: 19px; font-weight: 600; color: var(--red); }

  .compare { position: absolute; left: 28px; top: 274px; width: 523px; display: flex; gap: 13px; }
  .compare-col { width: 255px; height: 164px; border-radius: 6px; overflow: hidden; }
  .compare-col h2 { height: 34px; line-height: 34px; padding-left: 14px; font-size: 15px; font-weight: 800; letter-spacing: 1px; text-transform: uppercase; color: var(--paper); }
  .compare-col ul { list-style: none; padding: 10px 12px 0; }
  .compare-col li { display: flex; align-items: center; gap: 9px; height: 38px; font-size: 15.5px; font-weight: 600; }
  .compare-col svg { flex: none; }
  .risk { background: var(--red-soft); }
  .risk h2 { background: var(--red); }
  .expert { background: var(--blue-soft); }
  .expert h2 { background: var(--blue); }

  .experience { position: absolute; left: 28px; top: 452px; font-size: 17.5px; font-weight: 700; color: var(--blue-deep); }

  .audit-offer { position: absolute; left: 0; top: 488px; width: 579px; height: 158px; background: linear-gradient(180deg, var(--red) 0%, var(--red-deep) 100%); color: var(--paper); padding: 14px 28px 0; }
  .offer-kicker { font-size: 14px; font-weight: 800; letter-spacing: 3px; }
  .offer-title { font-family: "Merriweather", Georgia, serif; font-weight: 900; font-size: 28px; line-height: 36px; margin-top: 2px; }
  .offer-value { font-size: 17px; font-weight: 600; margin-top: 2px; }
  .offer-call { display: inline-block; margin-top: 10px; background: var(--paper); color: var(--red); font-size: 16px; font-weight: 800; padding: 6px 14px; border-radius: 4px; }
  .coupon-note { position: absolute; right: 28px; bottom: 14px; font-size: 14px; font-weight: 400; }

  .brand-strip { position: absolute; left: 0; top: 646px; width: 579px; height: 96px; background: var(--blue); color: var(--paper); padding: 16px 28px 0; }
  .trademark { font-family: "Merriweather", Georgia, serif; font-style: italic; font-weight: 400; font-size: 20px; line-height: 28px; }
  .brand-line { display: flex; align-items: center; gap: 10px; margin-top: 10px; font-size: 16px; }
  .brand-mark { width: 12px; height: 12px; background: var(--paper); }
  .brand-name { font-weight: 700; }
  .brand-web { font-weight: 400; margin-left: 8px; }

  .return-address { position: absolute; left: 600px; top: 96px; width: 280px; text-align: center; font-size: 18px; line-height: 21px; font-style: normal; color: var(--ink); }
  .return-address p { margin-bottom: 14px; }
  .return-address .sender { font-weight: 700; color: var(--blue-deep); }
  .stamp-box { position: absolute; left: 907px; top: 29px; width: 266px; height: 257px; border: 2px solid var(--rule); }
  .address-line { position: absolute; left: 645px; width: 497px; height: 2px; background: var(--rule); }
</style>
</head>
<body>
<main class="postcard">
  <section class="promo">
    <div class="team-photo" role="img" aria-label="Photo of experienced medical billing staff reviewing claims with providers"></div>

    <svg class="audit-seal" viewBox="0 0 124 124" aria-label="Free 10-chart/EOB audit">
      <circle cx="62" cy="62" r="61" fill="#ffffff"/>
      <circle cx="62" cy="62" r="55" fill="var(--red)"/>
      <circle cx="62" cy="62" r="48" fill="none" stroke="#ffffff" stroke-width="1.5" stroke-dasharray="4 3"/>
      <g font-family="Source Sans 3, Arial, sans-serif" font-weight="800" fill="#ffffff" text-anchor="middle">
        <text x="62" y="52" font-size="22">FREE</text>
        <text x="62" y="70" font-size="13.5">10-CHART/EOB</text>
        <text x="62" y="91" font-size="22">AUDIT*</text>
      </g>
    </svg>

    <header class="headline">
      <h1>Inexperience is expensive.</h1>
      <p>It’s what you DON’T know that is hurting you.</p>
    </header>

    <div class="compare">
      <div class="compare-col risk">
        <h2>New billing company</h2>
        <ul>
          <li><svg width="20" height="20" viewBox="0 0 20 20"><circle cx="10" cy="10" r="10" fill="var(--red)"/><path d="M6.5 6.5l7 7M13.5 6.5l-7 7" stroke="#fff" stroke-width="2.4" stroke-linecap="round"/></svg>Missed filing deadlines</li>
          <li><svg width="20" height="20" viewBox="0 0 20 20"><circle cx="10" cy="10" r="10" fill="var(--red)"/><path d="M6.5 6.5l7 7M13.5 6.5l-7 7" stroke="#fff" stroke-width="2.4" stroke-linecap="round"/></svg>Denials never appealed</li>
          <li><svg width="20" height="20" viewBox="0 0 20 20"><circle cx="10" cy="10" r="10" fill="var(--red)"/><path d="M6.5 6.5l7 7M13.5 6.5l-7 7" stroke="#fff" stroke-width="2.4" stroke-linecap="round"/></svg>Claims left to go to waste</li>
        </ul>
      </div>
      <div class="compare-col expert">
        <h2>25+ years of expertise</h2>
        <ul>
          <li><svg width="20" height="20" viewBox="0 0 20 20"><circle cx="10" cy="10" r="10" fill="var(--blue)"/><path d="M5.5 10.5l3 3 6-7" stroke="#fff" stroke-width="2.4" fill="none" stroke-linecap="round" stroke-linejoin="round"/></svg>Filed right the first time</li>
          <li><svg width="20" height="20" viewBox="0 0 20 20"><circle cx="10" cy="10" r="10" fill="var(--blue)"/><path d="M5.5 10.5l3 3 6-7" stroke="#fff" stroke-width="2.4" fill="none" stroke-linecap="round" stroke-linejoin="round"/></svg>Denials appealed &amp; paid</li>
          <li><svg width="20" height="20" viewBox="0 0 20 20"><circle cx="10" cy="10" r="10" fill="var(--blue)"/><path d="M5.5 10.5l3 3 6-7" stroke="#fff" stroke-width="2.4" fill="none" stroke-linecap="round" stroke-linejoin="round"/></svg>PPO / HMO / Vitacover</li>
        </ul>
      </div>
    </div>

    <p class="experience">Over 25 years in claims, billing, and revenue recovery.</p>

    <section class="audit-offer">
      <p class="offer-kicker">LIMITED-TIME OFFER</p>
      <p class="offer-title">FREE 10-CHART/EOB AUDIT</p>
      <p class="offer-value">A $500.00–$1,200.00 value. You can’t afford not to ask!</p>
      <p class="offer-call">Call (844) 783-3256 · Expires 30 days from mailing</p>
      <p class="coupon-note">*call for coupon code</p>
    </section>

    <footer class="brand-strip">
      <p class="trademark">Where Patience Pays &amp; Precision Prevails®</p>
      <p class="brand-line"><span class="brand-mark"></span><span class="brand-name">Steadfield Claims Desk</span><span class="brand-web">www.steadfieldclaimsdesk.com</span></p>
    </footer>
  </section>

  <address class="return-address">
    <p class="sender">Steadfield Claims Desk</p>
    <p>4870 Larkmoor Ave. #210-388<br>Fernhollow, CA 93512</p>
    <p>(844) STED CLM (783-3256)</p>
    <p>info@steadfieldclaimsdesk.com</p>
  </address>

  <div class="stamp-box"></div>
  <div class="address-line" style="top:407px"></div>
  <div class="address-line" style="top:488px"></div>
  <div class="address-line" style="top:568px"></div>
  <div class="address-line" style="top:648px"></div>
</main>
</body>
</html>
```